Packaging Design for Tidal Krill Blend 2400 MG

Project Overview:
Design a premium packaging box for Tidal Krill Blend 2400 MG capsules. The design should convey a balance between pharmaceutical credibility and luxury branding. The product is part of Q Vitalis’s high-end supplement line, and its visual identity should reflect both scientific integrity and elite status.

Product Details:
Name: Tidal Krill Blend 2400 MG

Box Dimensions: 83mm (W) x 41mm (D) x 112mm (H)

Brand: Q Vitalis

Key Ingredient: Omega-3 Fish Oil (High EPA & DHA)

Design Goals:
Simplicity & Sophistication:
A clean, minimal layout that avoids visual clutter while maintaining a high-end feel.

Pharmaceutical Aesthetic:
Should resemble a medical-grade product with a modern, science-driven aesthetic. Think clean lines, sharp typefaces, cool-toned color palettes (white, silver, dark gray, hints of cool blue).

Luxury Elements:
Incorporate luxury design cues—premium finishes like soft-touch matte or subtle foil stamping (e.g., silver or orange foiling). Avoid looking like a typical supplement; this is more of a boutique wellness product.

Branding:
Must prominently feature the Q Vitalis orange icon logo (attached) on the front or top panel—this is the main brand signature and should remain unaltered.

Target Audience:
Health-conscious professionals and affluent consumers aged 30–60 who prioritize premium wellness products and trust clinically-backed formulations.

Mandatory Elements:
Product Name: Tidal Krill Blend 2400 MG

Q Vitalis orange icon logo (attached)

Dimensions adhered to strictly

Space for supplement facts (on back or side panel)

UPC/Barcode placeholder (bottom or side)

FDA disclaimer (small text, back panel)

Tone & Style References:
Plumtree packaging (clean, clinical, elegant)

Verine or Le Sorbet (luxury meets minimalism)

Modern pharmaceutical branding (bioscience style fonts, Swiss layout influence)

Deliverables:
Box dieline design (print-ready, with bleed/crop marks)

3D mockup of the box (front + side view)

Editable source file (AI/PSD)

Industry/Entity Type

pharmaceutical / supplements retail

Colors
FFF300
FFF600
FEFA6F
FFFEC7
FFFEE8

Requirements
Must have
• Q Vitalis logo

```html
<!DOCTYPE html>
<html lang="en">
<head>
<meta charset="utf-8">
<title>Tidal Krill Blend 2400 MG — Packaging</title>
<link rel="stylesheet" href="https://fonts.googleapis.com/css2?family=Montserrat:wght@700;800&family=Sora:wght@400;500;600&display=swap">
<style>
  :root{
    --stage:#f1f1f0;
    --panel:#e7e7e5;
    --panel-light:#efefed;
    --ink:#2a2a2c;
    --ink-soft:#3a3a3d;
    --orange:#e2711d;
    --band:#2a2a2c;
    --silver:#a3a3a3;
    --on-dark:#e9e9e9;
  }
  *{box-sizing:border-box;margin:0;padding:0}
  html,body{width:1200px;height:902px;overflow:hidden}
  body{background:var(--stage);font-family:"Sora",sans-serif;color:var(--ink);position:relative}

  .box{position:absolute;top:71px;height:760px;overflow:hidden}
  .side-panel{left:178px;width:278px;background:linear-gradient(180deg,var(--panel-light),var(--panel))}
  .front-panel{left:456px;width:563px;background:var(--panel)}
  .panel-art{position:absolute;inset:0}

  /* brand */
  .brand{position:absolute;display:flex;align-items:center;gap:10px}
  .brand-dot{width:30px;height:30px;border-radius:50%;background:var(--orange)}
  .brand-name{font-family:"Sora",sans-serif;font-weight:600;color:var(--ink-soft);letter-spacing:.5px}
  .front-panel .brand{left:54px;top:78px}
  .front-panel .brand-name{font-size:30px}

  /* front copy */
  .product-title{position:absolute;left:50px;top:170px;font-family:"Montserrat",sans-serif;font-weight:800;font-size:66px;line-height:76px;color:var(--ink);letter-spacing:1px}
  .dose{position:absolute;left:54px;top:338px;font-family:"Montserrat",sans-serif;font-weight:700;font-size:56px;color:var(--orange);letter-spacing:1px}
  .formula{position:absolute;left:54px;top:414px;font-weight:600;font-size:27px;line-height:33px;color:var(--ink)}
  .rule{position:absolute;left:56px;top:497px;width:354px;height:3px;background:var(--ink)}
  .pill{position:absolute;left:56px;top:514px;padding:3px 14px;border:2px solid var(--ink);border-radius:22px;font-size:27px;font-weight:400;color:var(--ink)}
  .claim{position:absolute;left:74px;top:558px;font-size:18px;color:var(--ink)}
  .count{position:absolute;left:56px;top:605px;display:flex;align-items:center;gap:10px;padding:6px 16px;background:var(--orange);border-radius:8px;color:#fff;font-weight:500;font-size:24px}
  .benefit{position:absolute;left:54px;top:668px;display:flex;align-items:center;gap:12px;color:var(--on-dark);font-size:19px;line-height:22px}
  .benefit-icon{width:42px;height:42px}
  .benefit-divider{width:2px;height:44px;background:var(--on-dark)}
  .source{position:absolute;right:20px;top:684px;text-align:right;color:var(--on-dark);font-size:19px;line-height:25px}

  /* side copy */
  .side-panel .brand{left:24px;top:60px;gap:6px}
  .side-panel .brand-dot{width:14px;height:14px}
  .side-panel .brand-name{font-size:14px}
  .side-title{position:absolute;left:24px;top:102px;font-family:"Montserrat",sans-serif;font-weight:800;font-size:17px;color:var(--ink)}
  .side-copy{position:absolute;left:24px;top:150px;width:230px;font-size:11px;line-height:16px;color:var(--ink-soft)}
  .side-copy h3{font-size:11px;font-weight:600;color:var(--orange);margin-top:14px}
  .side-copy h3:first-child{margin-top:0}
  .side-copy p{margin-top:2px}
  .made-in{position:absolute;left:24px;bottom:40px;font-size:10px;color:var(--on-dark);letter-spacing:.5px}
</style>
</head>
<body>

<section class="box side-panel" aria-label="Side panel">
  <svg class="panel-art" viewBox="0 0 278 760" aria-hidden="true">
    <rect x="0" y="624" width="278" height="8" fill="#9d9d9d"/>
    <rect x="0" y="632" width="278" height="128" fill="#2a2a2c"/>
  </svg>
  <div class="brand"><span class="brand-dot"></span><span class="brand-name">Q Vitalis</span></div>
  <h2 class="side-title">TIDAL KRILL BLEND</h2>
  <div class="side-copy">
    <h3>Suggested Use:</h3>
    <p>Take one softgel daily with food.</p>
    <h3>Key Ingredients:</h3>
    <p>Omega-3 Fatty Acids 2400mg<br>EPA (Eicosapentaenoic Acid) 720mg<br>DHA (Docosahexaenoic Acid) 480mg</p>
    <h3></h3>
    <p>May help support a healthy heart and brain function.</p>
    <p style="margin-top:14px">Trusted formula. Committed to premium quality and purity.</p>
  </div>
  <p class="made-in">Made in the US</p>
</section>

<section class="box front-panel" aria-label="Front panel">
  <svg class="panel-art" viewBox="0 0 563 760" aria-hidden="true">
    <defs>
      <linearGradient id="shade" x1="0" y1="0" x2="0" y2="1">
        <stop offset="0.3" stop-color="#ececea"/>
        <stop offset="0.62" stop-color="#9b9b9c"/>
        <stop offset="0.85" stop-color="#3a3a3c"/>
        <stop offset="1" stop-color="#2a2a2c"/>
      </linearGradient>
      <linearGradient id="swoosh" x1="0" y1="1" x2="1" y2="0">
        <stop offset="0" stop-color="#8c8c8c"/>
        <stop offset="0.5" stop-color="#dcdcdc"/>
        <stop offset="1" stop-color="#9a9a9a"/>
      </linearGradient>
    </defs>
    <rect x="0" y="624" width="563" height="8" fill="#9d9d9d"/>
    <rect x="0" y="632" width="563" height="128" fill="#2a2a2c"/>
    <path d="M563 230 C470 400 330 620 245 760 L563 760 Z" fill="url(#shade)"/>
    <path d="M563 222 C470 395 330 615 238 760" fill="none" stroke="url(#swoosh)" stroke-width="14"/>
  </svg>
  <svg class="panel-art" viewBox="0 0 563 760" role="img" aria-label="Faint DNA helix and hexagon molecule pattern">
    <ellipse cx="400" cy="330" rx="130" ry="260" fill="#ffffff" opacity="0.22"/>
    <ellipse cx="470" cy="560" rx="90" ry="110" fill="#5a5a5c" opacity="0.25"/>
  </svg>

  <div class="brand"><span class="brand-dot"></span><span class="brand-name">Q Vitalis</span></div>
  <h1 class="product-title">TIDAL KRILL<br>BLEND</h1>
  <p class="dose">2400 MG</p>
  <p class="formula">High Potency Omega-3<br>Formula.</p>
  <div class="rule"></div>
  <p class="pill">Dietary Supplement</p>
  <p class="claim">With High EPA &amp; DHA</p>
  <p class="count">
    <svg width="20" height="20" viewBox="0 0 20 20" aria-hidden="true"><path d="M10 0 C11 7 13 9 20 10 C13 11 11 13 10 20 C9 13 7 11 0 10 C7 9 9 7 10 0Z" fill="#fff"/></svg>
    60 Softgels
  </p>
  <div class="benefit">
    <svg class="benefit-icon" viewBox="0 0 42 42" role="img" aria-label="Brain icon"><circle cx="21" cy="21" r="17" fill="none" stroke="#e9e9e9" stroke-width="2.5" stroke-dasharray="5 3"/><circle cx="21" cy="21" r="9" fill="#e9e9e9"/></svg>
    <span class="benefit-divider"></span>
    <span>Suppot Brain<br>Function</span>
  </div>
  <p class="source">Sourced from Pure<br>Fish Oils.</p>
</section>

</body>
</html>
```